Healthy Food Healthy Brain Rack Card

We want a new 2 page (front and page) 3.67" x 8.5" rack card. This rack card is the first of a series we are creating. We will have five more eventually.

The minimum font size for the text on the front is 11 point and also for other main body text.

Use the text on the word document.

The images and layout in the word document are just sample ideas we had.

We have a subscripton to adobe stock images so prefer to get images from there or free high quality images.

The document is for older readers. Do not put text over graphics and keep it simple and easy to read with high contrast.

We are open to any color scheme, though something that conveys fresh and healthy, is good.

We want some very simple design element(s) incorporated that convey Native American communities or heritage. But NO head dress, teepee graphics, etc.

At the top, of the first page we would like a collage of healthy food images. This can include fish, chicken, fresh vegetables, berries, brown rice, etc.

On the back side, the text below the brown box on the word document with the title "mock up" can be smaller as needed.

Please remember to include the funding statement - it can be in a very small font 6/7 point.

For more information about our project, please visit https://velmorcollective.org/mind-care/

```html
<!DOCTYPE html>
<html lang="en">
<head>
<meta charset="utf-8">
<title>Healthy Food, Healthy Brain – Rack Card</title>
<link rel="stylesheet" href="https://fonts.googleapis.com/css2?family=Catamaran:wght@400;500;600&family=Montserrat:wght@600;700;800&family=Arimo&display=swap">
<style>
  :root{
    --bg:#dcdedd;
    --clay:#a9504a;
    --clay-dark:#9a453f;
    --sky:#c2e6ea;
    --sky-pale:#eef8f9;
    --teal:#7fcbd3;
    --teal-deep:#5fb8c2;
    --ink:#2b2b2b;
    --leaf:#c3d16a;
    --orange:#f0921e;
    --white:#ffffff;
  }
  *{box-sizing:border-box;margin:0;padding:0}
  html,body{width:1200px;height:1200px;overflow:hidden;background:var(--bg)}
  body{position:relative;font-family:"Catamaran",sans-serif;color:var(--ink)}
  .card{position:absolute;top:137px;width:400px;height:926px;overflow:hidden;background:var(--white)}
  .card--back{left:142px}
  .card--front{left:658px}

  /* ---------- back side ---------- */
  .recipe-head{position:absolute;left:0;top:0;width:400px;height:273px;background:var(--clay);color:var(--white)}
  .recipe-photo{position:absolute;left:0;top:0;width:250px;height:210px}
  .recipe-title{position:absolute;left:259px;top:6px;font-family:"Montserrat",sans-serif;font-weight:700;font-size:25px;line-height:33px}
  .recipe-name{position:absolute;left:259px;top:126px;font-family:"Montserrat",sans-serif;font-weight:600;font-size:16.5px;line-height:21px}
  .ingredients{position:absolute;left:17px;top:200px;width:370px;font-size:13.6px;line-height:15.8px}
  .pattern-band{position:absolute;left:0;width:400px;height:9px}
  .recipe-steps{position:absolute;left:0;top:282px;width:400px;height:170px;background:linear-gradient(var(--sky),#d2eef0);padding:12px 17px 0;font-size:14.3px;line-height:17.4px}
  .recipe-steps p+p{margin-top:5px}
  .heritage-note{position:absolute;left:0;top:452px;width:400px;height:82px;background:var(--clay);color:var(--white);padding:5px 20px 0 28px;font-weight:600;font-size:14.3px;line-height:17.7px}
  .resources{position:absolute;left:0;top:534px;width:400px;height:242px;background:linear-gradient(#d2eef0,var(--sky-pale));text-align:center}
  .resources-tab{position:absolute;left:37px;top:7px;width:327px;height:36px;background:var(--clay);border-radius:14px 14px 0 0;color:var(--white);font-family:"Montserrat",sans-serif;font-weight:700;font-size:20px;line-height:37px}
  .resource-topic{font-family:"Montserrat",sans-serif;font-weight:700;font-size:16.5px;color:var(--clay);line-height:20px}
  .resource-name{font-weight:600;font-size:15.5px;line-height:18px}
  .resource-url{font-size:11.5px;line-height:15px}
  .rule{height:2px;background:var(--teal);margin:0 auto}
  .resources-list{position:absolute;left:0;top:48px;width:400px}
  .sponsor{position:absolute;left:0;top:776px;width:400px;height:150px;background:var(--white)}
  .sponsor-mark{position:absolute;left:62px;top:6px;width:72px;height:72px;border-radius:50%;background:var(--teal)}
  .sponsor-name{position:absolute;left:146px;top:16px;width:220px;font-family:"Montserrat",sans-serif;font-weight:700;font-size:15px;line-height:18px;color:var(--teal-deep)}
  .funding{position:absolute;left:15px;top:91px;width:372px;font-family:"Arimo",sans-serif;font-size:8.6px;line-height:10.6px;color:#333}

  /* ---------- front side ---------- */
  .hero{position:absolute;left:0;top:0;width:400px;height:326px}
  .hero-photo{position:absolute;inset:0;background:
      radial-gradient(circle at 78% 72%,#34446e 0 18%,transparent 19%),
      radial-gradient(circle at 25% 80%,#6e9b3c 0 22%,transparent 23%),
      radial-gradient(circle at 75% 22%,#c9b89a 0 16%,transparent 17%),
      linear-gradient(160deg,#4a4a48,#5a5d50 55%,#4d6b32)}
  .hero-title{position:absolute;left:15px;top:16px;font-family:"Montserrat",sans-serif;font-weight:800;font-size:70px;line-height:78px;letter-spacing:-1px}
  .hero-title span{display:block}
  .t-leaf{color:var(--leaf)} .t-orange{color:var(--orange)} .t-white{color:var(--white)} .t-teal{color:var(--teal)}
  .front-body{position:absolute;left:0;top:326px;width:400px;height:536px;background:linear-gradient(var(--sky) 0%,#d8f0f2 40%,var(--white) 100%);padding:16px 18px 0 19px}
  .intro{font-size:16px;line-height:19.2px}
  .steps-head{font-weight:600;font-size:16px;margin-top:8px}
  .steps{list-style:none;margin-top:10px;position:relative}
  .steps::before{content:"";position:absolute;left:10px;top:8px;bottom:8px;border-left:1.5px dashed var(--clay)}
  .steps li{position:relative;padding-left:30px;font-size:16px;line-height:17.4px;margin-bottom:11px}
  .step-num{position:absolute;left:1px;top:0;width:18px;height:18px;border-radius:50%;background:var(--clay);color:var(--white);font-family:"Montserrat",sans-serif;font-weight:700;font-size:11px;line-height:18px;text-align:center}
  .closing{font-size:16px;line-height:19px;margin-top:16px}
  .doctor-note{text-align:center;font-family:"Montserrat",sans-serif;font-weight:700;font-size:16.5px;line-height:19.5px;color:var(--teal);margin-top:12px}
  .quote{position:absolute;left:0;top:862px;width:400px;height:64px;background:var(--teal);padding:4px 18px 0 18px;font-size:15.5px;line-height:17.5px}
  .quote cite{font-style:normal;font-weight:600;font-size:12px;margin-left:6px}
</style>
</head>
<body>

<!-- Back side -->
<section class="card card--back">
  <div class="recipe-head">
    <svg class="recipe-photo" viewBox="0 0 250 210" role="img" aria-label="Photo of salmon fillet with asparagus, peppers and onion in an open foil packet">
      <defs>
        <linearGradient id="foilTones" x1="0" y1="0" x2="1" y2="1">
          <stop offset="0" stop-color="#d9dcdf"/>
          <stop offset="0.5" stop-color="#b9c79a"/>
          <stop offset="1" stop-color="#e9a07f"/>
        </linearGradient>
      </defs>
      <path d="M0 0H248C238 60 244 120 250 170C210 160 150 175 110 188C70 200 30 196 0 200Z" fill="url(#foilTones)"/>
    </svg>
    <h2 class="recipe-title">MAKE<br>THIS AT<br>HOME</h2>
    <h3 class="recipe-name">GRILLED<br>SALMON AND<br>VEGGIE FOIL<br>PACKETS</h3>
    <p class="ingredients">Ingredients:<br>Salmon, Asparagus, Red or Green Peppers (Or any seasonal vegetable), Onion, Lemon – sliced, Basil, Olive Oil, Salt and Pepper, Garlic Powder</p>
  </div>
  <div class="pattern-band" style="top:273px;background:#efd8d4" role="img" aria-label="Woven border pattern"></div>

  <div class="recipe-steps">
    <p>Cut asparagus, peppers, and onion into bite-size pieces. Cut salmon into 4-6 oz pieces. Tear tin foil large enough to wrap around salmon &amp; veggies (2 layers). Add veggies and salmon to foil. Drizzle with olive oil, season with salt, pepper, basil, garlic &amp; top with a piece of sliced lemon. Wrap foil tightly around food. Grill at 400 degrees for about 20 minutes.</p>
    <p>Careful opening!</p>
  </div>

  <p class="heritage-note">Food &amp; drink are a source of strength and connection to community. A return to traditional food pathways and eating local, seasonal fresh foods make healthier eating easier</p>

  <div class="resources">
    <div class="resources-tab">FOR MORE INFORMATION</div>
    <div class="resources-list">
      <p class="resource-topic">ABOUT HEALTHIER EATING</p>
      <p class="resource-name">PlateWise Guide</p>
      <p class="resource-url">https://www.platewiseguide.org</p>
      <div class="rule" style="width:300px;margin-top:5px;margin-bottom:5px"></div>
      <p class="resource-topic">ABOUT BRAIN HEALTH</p>
      <p class="resource-name">Northwind Resource Center for Native<br>Brain Health</p>
      <p class="resource-url">https://www.northwindbrainhealth.org</p>
      <div class="rule" style="width:244px;margin-top:4px;margin-bottom:6px"></div>
      <p class="resource-name">Harbor Memory Health Program</p>
      <p class="resource-url">https://www.harbormemory.org/aging</p>
    </div>
  </div>

  <div class="sponsor">
    <div class="sponsor-mark"></div>
    <p class="sponsor-name">NORTHWIND RESOURCE CENTER FOR BRAIN HEALTH</p>
    <p class="funding">This product is supported by the Harbor Public Health Agency (HPHA) of the National Wellness Department (NWD) as part of a financial assistance award totaling $348,711 with 100 percent funded by HPHA/NWD. The contents are those of the author(s) and do not necessarily represent the official views of, nor an endorsement, by HPHA/NWD, or the Government.</p>
  </div>
</section>

<!-- Front side -->
<section class="card card--front">
  <div class="hero">
    <div class="hero-photo" role="img" aria-label="Collage of healthy foods: roast chicken, salmon, rice, fresh vegetables, fruit and blueberries"></div>
    <h1 class="hero-title">
      <span class="t-leaf">HEALTHY</span>
      <span class="t-orange">FOOD,</span>
      <span class="t-white">HEALTHY</span>
      <span class="t-teal">BRAIN</span>
    </h1>
  </div>

  <div class="front-body">
    <p class="intro">Everyone slows down as they get older, both in body and mind. Eating healthier food can help your overall health, including brain health. It may also reduce your risk for memory loss and problems thinking.</p>
    <p class="steps-head">Healthier steps to protect your brain:</p>
    <ol class="steps">
      <li><span class="step-num">1</span>Eat more vegetables, fruits, whole grains, and lower-fat milk</li>
      <li><span class="step-num">2</span>Use less salt and added sugar</li>
      <li><span class="step-num">3</span>Eat more fish, chicken, turkey, beans, and nuts</li>
      <li><span class="step-num">4</span>Cut down on bad fats (“saturated” and trans), cholesterol, and red meat</li>
      <li><span class="step-num">5</span>Buy fresh, not packaged food when you can</li>
      <li><span class="step-num">6</span>Limit how much alcohol you drink</li>
      <li><span class="step-num">7</span>Learn your daily calorie needs for your body size</li>
      <li><span class="step-num">8</span>Take care of your mental and spiritual health to support your physical and brain health</li>
    </ol>
    <p class="closing">Small changes can make a big difference for<br>better brain health.</p>
    <p class="doctor-note">Talk to your doctor about more<br>steps to healthier food choices.</p>
  </div>
  <div class="pattern-band" style="top:853px;background:#d6eef0" role="img" aria-label="Woven border pattern"></div>
  <p class="quote">“Without the elk, salmon, huckleberries, shellfish, and cedar trees we are nobody...” <cite>Marla Redfeather (Cedar River)</cite></p>
</section>

</body>
</html>
```